Invoice design

Please design an invoice like the attached

- Please include a logo in the header (any logo rectangular is fine)

- We do not need a DUE DATE on the invoice (next to the total inc. vat)

- For each product put in smaller text beneath which might contain additional information about the product (e.g. size, colour choices)

- Do not put a signature in the footer

```html
<!DOCTYPE html>
<html lang="en">
<head>
<meta charset="utf-8">
<title>Invoice 00001</title>
<link rel="stylesheet" href="https://fonts.googleapis.com/css2?family=Jost:wght@400&family=Open+Sans:wght@400;600;700&display=swap">
<style>
:root{
  --brand:#2d6089;
  --ink:#4a4a4a;
  --ink-soft:#8a8a8a;
  --rule:#c9c9c9;
  --footer:#e3e4e6;
  --paper:#ffffff;
  --backdrop:#eef1f4;
}
*{box-sizing:border-box;margin:0;padding:0}
html,body{width:920px;height:1200px;overflow:hidden}
body{background:var(--backdrop);font-family:"Open Sans",Arial,sans-serif;color:var(--ink)}
.invoice{position:absolute;left:47px;top:16px;width:826px;height:1168px;background:var(--paper);box-shadow:0 6px 24px rgba(0,0,0,.12);overflow:hidden}
.abs{position:absolute}
.top-band{left:0;top:0;width:100%;height:21px;background:var(--brand)}
.brand{display:flex;align-items:center;gap:12px;color:var(--brand);font-family:"Jost",sans-serif;font-weight:400;line-height:1}
.brand-square{border:2px solid var(--brand);flex:none}
.brand-header{left:58px;top:43px}
.brand-header .brand-square{width:51px;height:51px}
.brand-header .brand-name{font-size:34px;letter-spacing:.5px}
.header-contact{right:60px;top:36px;text-align:right;color:var(--brand);line-height:1.2}
.header-contact div{display:flex;justify-content:flex-end;align-items:center;gap:6px}
.header-contact .phone{font-size:21px;font-weight:600}
.header-contact .email{font-size:14px}
.header-contact .web{font-size:16px;font-weight:600}
.icon-solid{fill:var(--brand)}
.icon-line{fill:none;stroke:var(--brand);stroke-width:1.8}
.header-rule{left:55px;top:117px;width:712px;height:2px;background:var(--brand)}
.title{left:55px;top:150px;font-family:"Jost",sans-serif;font-weight:400;font-size:64px;color:var(--brand);line-height:1;letter-spacing:-.5px}
.meta{left:58px;top:237px;display:flex;flex-direction:column;gap:17px}
.label{color:var(--brand);font-weight:600;font-size:15.5px;line-height:1.15;text-transform:uppercase}
.value{font-size:15.5px;line-height:1.2;font-weight:400;color:var(--ink)}
.divider-v{width:2px;background:var(--brand)}
.divider-parties{left:326px;top:166px;height:297px}
.party{left:358px;line-height:18.6px;font-size:15.5px;font-weight:400}
.party .label{line-height:18px}
.party-supplier{top:164px}
.party-client{top:316px}
.items{left:55px;top:505px;width:712px}
.items-head,.item-row{display:grid;grid-template-columns:213px 120px 101px 172px 55px 51px;align-items:start;white-space:nowrap}
.items-head{color:var(--brand);font-weight:600;font-size:14px;height:36px;padding-top:6px;border-bottom:2px solid var(--brand)}
.items-head span:last-child{text-align:right}
.item-row{height:38px;padding-top:11px;border-bottom:1.5px solid var(--rule);font-size:12px;color:var(--ink-soft)}
.item-row:last-child{height:40px}
.item-name{color:var(--ink);font-weight:600;line-height:1.1}
.item-detail{display:block;font-size:8.5px;font-weight:400;color:var(--ink-soft);line-height:1.2}
.item-row .desc{margin-left:-4px}
.item-row .qty{padding-left:29px}
.item-row .price{text-align:right;padding-right:41px}
.item-row .vat{padding-left:2px}
.item-row .total{text-align:right;overflow:visible;direction:rtl}
.totals{left:420px;top:628px;width:347px}
.totals-row{display:flex;justify-content:space-between;align-items:center;height:40.5px;border-bottom:1.5px solid var(--rule);font-size:15.5px}
.totals-row:last-child{border-bottom:none}
.totals-row .amount{font-weight:700;color:var(--ink)}
.grand{left:55px;top:786px;width:713px;height:53px;border:2.5px dotted var(--brand);display:flex;align-items:center;padding-left:363px;padding-right:19px;justify-content:space-between}
.grand .amount{font-size:25px;font-weight:700;color:var(--brand)}
.footer{left:0;top:884px;width:100%;height:284px;background:var(--footer)}
.footer-notch{left:394px;top:884px}
.thanks{left:55px;top:930px;font-size:12.5px}
.brand-footer{left:54px;top:1015px;gap:10px}
.brand-footer .brand-square{width:41px;height:41px}
.brand-footer .brand-name{font-size:26px;letter-spacing:.4px}
.divider-payment{left:565px;top:934px;height:124px}
.payment{left:595px;top:928px;display:flex;flex-direction:column;gap:8px}
.payment .label,.payment .value{font-size:14.5px}
.footer-rule{left:55px;top:1087px;width:713px;height:1.5px;background:var(--rule)}
.footer-contact{left:0;top:1104px;width:100%;display:flex;justify-content:center;gap:20px;font-size:12.5px;color:var(--ink)}
.footer-contact span{display:flex;align-items:center;gap:7px}
.social-dot{width:11px;height:11px;border:1.5px solid var(--brand);border-radius:50%}
</style>
</head>
<body>
<main class="invoice">
  <div class="abs top-band"></div>

  <div class="abs brand brand-header">
    <div class="brand-square"></div>
    <span class="brand-name">NORTHMERE</span>
  </div>

  <div class="abs header-contact">
    <div class="phone"><svg class="icon-solid" width="15" height="15" viewBox="0 0 24 24"><path d="M6.6 10.8a15.5 15.5 0 0 0 6.6 6.6l2.2-2.2c.3-.3.7-.4 1-.2 1.1.4 2.3.6 3.6.6.6 0 1 .4 1 1V20c0 .6-.4 1-1 1A17 17 0 0 1 3 4c0-.6.4-1 1-1h3.5c.6 0 1 .4 1 1 0 1.3.2 2.5.6 3.6.1.3 0 .7-.2 1z"/></svg>+44 1632 960418</div>
    <div class="email"><svg class="icon-solid" width="16" height="12" viewBox="0 0 24 18"><path d="M0 0h24v18H0z M2 2v1l10 7 10-7V2z" fill-rule="evenodd"/></svg>hello@northmere.co.uk</div>
    <div class="web"><svg class="icon-line" width="15" height="15" viewBox="0 0 24 24"><circle cx="12" cy="12" r="10"/><ellipse cx="12" cy="12" rx="4.5" ry="10"/><path d="M2 12h20M4 7h16M4 17h16"/></svg>www.northmere.co.uk</div>
  </div>

  <div class="abs header-rule"></div>

  <h1 class="abs title">INVOICE</h1>

  <section class="abs meta">
    <div><div class="label">Invoice:</div><div class="value">00001</div></div>
    <div><div class="label">Issue date:</div><div class="value">July 3,2024</div></div>
    <div><div class="label">Delivery date</div><div class="value">July 3,2024</div></div>
    <div><div class="label">Due date:</div><div class="value">July 18,2024</div></div>
  </section>

  <div class="abs divider-v divider-parties"></div>

  <section class="abs party party-supplier">
    <div class="label">Supplier</div>
    <div>Harwick Trading Ltd</div>
    <div>42 Alder Lane</div>
    <div>London</div>
    <div>EC1V 4QT</div>
    <div>United Kigdom</div>
    <div>VAT No: GB5550123456</div>
  </section>

  <section class="abs party party-client">
    <div class="label">Client</div>
    <div>Thomas Ridley</div>
    <div>The Copper Kettle</div>
    <div>17 Fenwick Street</div>
    <div>London</div>
    <div>NW5 2LP</div>
    <div>United Kingdom</div>
    <div>VAT No: GB987 6543 21</div>
  </section>

  <section class="abs items">
    <div class="items-head">
      <span>Item</span><span>Description</span><span>Quantity</span><span>Unit Price incl. VAT</span><span>VAT</span><span>Total</span>
    </div>
    <div class="item-row">
      <span class="item-name">Highland Estate Reserve<span class="item-detail">Color: Black | Size: 5</span></span>
      <span class="desc">1 kg / Full City</span><span class="qty">2</span><span class="price">15.00</span><span class="vat">20%</span><span class="total">£30.00</span>
    </div>
    <div class="item-row">
      <span class="item-name">Valley Ridge - Santa Lucia<span class="item-detail">Color: Black | Size: 5</span></span>
      <span class="desc">1 kg / Full City</span><span class="qty">3</span><span class="price">65.00</span><span class="vat">20%</span><span class="total">£195.00</span>
    </div>
  </section>

  <section class="abs totals">
    <div class="totals-row"><span class="label">Subtotal:</span><span class="amount">£225.00</span></div>
    <div class="totals-row"><span class="label">Shipping:</span><span class="amount">£18.00</span></div>
    <div class="totals-row"><span class="label">Total excl. VAT:</span><span class="amount">£205.50</span></div>
    <div class="totals-row"><span class="label">VAT 20%:</span><span class="amount">£37.50</span></div>
  </section>

  <div class="abs grand">
    <span class="label">Total incl. VAT:</span>
    <span class="amount">£243.00</span>
  </div>

  <footer class="abs footer"></footer>
  <svg class="abs footer-notch" width="40" height="18" viewBox="0 0 40 18"><path d="M0 0h40L20 18z" fill="#ffffff"/></svg>

  <p class="abs thanks">Thank you for your purchase.</p>

  <div class="abs brand brand-footer">
    <div class="brand-square"></div>
    <span class="brand-name">NORTHMERE</span>
  </div>

  <div class="abs divider-v divider-payment"></div>

  <section class="abs payment">
    <div><div class="label">Payment method</div><div class="value">Bank Transfer</div></div>
    <div><div class="label">Bank account</div><div class="value">4021 0000 3318 2265</div></div>
    <div><div class="label">Order number</div><div class="value">#1029</div></div>
  </section>

  <div class="abs footer-rule"></div>

  <div class="abs footer-contact">
    <span><svg class="icon-solid" width="13" height="13" viewBox="0 0 24 24"><path d="M6.6 10.8a15.5 15.5 0 0 0 6.6 6.6l2.2-2.2c.3-.3.7-.4 1-.2 1.1.4 2.3.6 3.6.6.6 0 1 .4 1 1V20c0 .6-.4 1-1 1A17 17 0 0 1 3 4c0-.6.4-1 1-1h3.5c.6 0 1 .4 1 1 0 1.3.2 2.5.6 3.6.1.3 0 .7-.2 1z"/></svg>+44 1632 960418</span>
    <span><svg class="icon-solid" width="15" height="11" viewBox="0 0 24 18"><path d="M0 0h24v18H0z M2 2v1l10 7 10-7V2z" fill-rule="evenodd"/></svg>hello@northmere.co.uk</span>
    <span><svg class="icon-line" width="13" height="13" viewBox="0 0 24 24"><circle cx="12" cy="12" r="10"/><ellipse cx="12" cy="12" rx="4.5" ry="10"/><path d="M2 12h20M4 7h16M4 17h16"/></svg>www.northmere.co.uk</span>
    <span><i class="social-dot"></i>@northmere</span>
  </div>
</main>
</body>
</html>
```